Business Card Design Project

I need a business card design for our new logo, please check the logo at the following link:
https://www.filecrate.net/s/q7rtx2pw9kd41m/FernLoop.png
The address on the business card:
Av. Gervásio Tavares 418 sala 207
Barra da Tijuca, Rio de Janeiro, RJ
CEP: 22714-380
Brasil
Phone: +55 21 86347215
e-mail: osvaldo@fernloop.com.br
Updates
Thank you all for sending your designs, we will not provide feedback because there are too many designs, on December 3 we will pick the best design according to our point of view. Please keep posting.
Osvaldo
Industry/Entity Type
Business
Look and feel
Each slider illustrates characteristics of the customer's brand and the style your logo design should communicate.

```html
<!DOCTYPE html>
<html lang="pt-BR">
<head>
<meta charset="utf-8">
<title>FernLoop – Cartão de Visita</title>
<link href="https://fonts.googleapis.com/css2?family=Crimson+Text:wght@400;700&display=swap" rel="stylesheet">
<style>
  :root {
    --backdrop: #ece8e2;
    --card-white: #ffffff;
    --brand-yellow: #f7c81a;
    --brand-yellow-deep: #eeb70c;
    --swoosh-grey: #c9c9c9;
    --ink: #1a1a1a;
    --ink-soft: #2b2b2b;
  }
  * { margin: 0; padding: 0; box-sizing: border-box; }
  html, body {
    width: 1200px;
    height: 811px;
    overflow: hidden;
    background: var(--backdrop);
  }
  .business-card {
    position: absolute;
    left: 150px;
    top: 145px;
    width: 900px;
    height: 522px;
    background: var(--card-white);
    box-shadow: 0 10px 30px rgba(0,0,0,0.18);
    overflow: hidden;
    font-family: "Crimson Text", Georgia, serif;
    color: var(--ink);
  }
  .card-waves {
    position: absolute;
    inset: 0;
  }
  .logo-block {
    position: absolute;
    left: 70px;
    top: 155px;
    width: 240px;
  }
  .logo-illustration {
    width: 190px;
    height: 150px;
    margin-left: 20px;
    border-radius: 6px;
    background: linear-gradient(135deg, #2a2a2a 0%, #3a3a3a 60%, var(--brand-yellow) 100%);
  }
  .brand-name {
    margin-top: 8px;
    font-size: 56px;
    font-weight: 700;
    line-height: 1;
    color: var(--ink);
  }
  .contact-block {
    position: absolute;
    right: 40px;
    top: 135px;
    text-align: right;
  }
  .address-line {
    font-size: 26px;
    line-height: 31px;
    color: var(--ink-soft);
  }
  .phone {
    margin-top: 34px;
    font-size: 32px;
    font-weight: 700;
    line-height: 38px;
  }
  .email {
    font-size: 26px;
    line-height: 32px;
    color: var(--ink-soft);
  }
</style>
</head>
<body>
  <div class="business-card">
    <svg class="card-waves" viewBox="0 0 900 522" preserveAspectRatio="none" aria-hidden="true">
      <defs>
        <linearGradient id="yellowFill" x1="0" y1="0" x2="0" y2="1">
          <stop offset="0" stop-color="var(--brand-yellow)"/>
          <stop offset="1" stop-color="var(--brand-yellow-deep)"/>
        </linearGradient>
      </defs>
      <!-- top band -->
      <path d="M0 0 H900 V28 C700 40 560 70 360 76 C200 80 80 90 0 120 Z" fill="url(#yellowFill)"/>
      <path d="M0 128 C80 98 200 88 360 84 C560 78 700 48 900 36 V28 C700 40 560 70 360 76 C200 80 80 90 0 120 Z" fill="var(--swoosh-grey)"/>
      <!-- bottom band -->
      <path d="M0 440 C200 470 400 470 560 440 C700 414 800 398 900 392 V382 C800 388 700 404 560 430 C400 460 200 460 0 428 Z" fill="var(--swoosh-grey)"/>
      <path d="M0 448 C200 478 400 478 560 448 C700 422 800 406 900 400 V522 H0 Z" fill="url(#yellowFill)"/>
    </svg>

    <div class="logo-block">
      <div class="logo-illustration" role="img" aria-label="Brand mascot illustration"></div>
      <div class="brand-name">FernLoop</div>
    </div>

    <div class="contact-block">
      <p class="address-line">Av. Gervásio Tavares 418 sala 207</p>
      <p class="address-line">Barra da Tijuca, Rio de Janeiro, RJ</p>
      <p class="address-line">CEP: 22714-380</p>
      <p class="address-line">Brasil</p>
      <p class="phone">Phone: +55 21 86347215</p>
      <p class="email">e-mail: osvaldo@fernloop.com.br</p>
    </div>
  </div>
</body>
</html>
```